Multi Disciplinary Health Clinic Needs a Pop Up Banner

Brightway Health needs a pop up banner ( approx. 33" x 80") to use at marketing events. We offer Chiropractic, Massage Therapy, Acupuncture, Laser Therapy, Shockwave Therapy and a lot of other modalities. We have a diverse client base ranging from children to professional athletes. More info about our clinic can be found at www.brightwayhealth.ca

Target Market(s)

potential patients, all age ranges, people who are in pain or are wanting to improve their health

Industry/Entity Type

Health And Wellness

Font styles to use
Sans Serif

Requirements
Must have
• our logo
• serives: chiropractic, massage therapy, shockwave, laser
• our logo colours as the basis for the colour theme
• our website address
Nice to have
• our phone number
• images from our website ( i have high resolution files of all images)
• word font that fits with our logo font
Should not have
• an abundance of spa massage pictures. we focus more on the rehabilitation of pain and injury.

```html
<!DOCTYPE html>
<html lang="en">
<head>
<meta charset="utf-8">
<title>Brightway Health – Pop Up Banner</title>
<link rel="stylesheet" href="https://fonts.googleapis.com/css2?family=Arimo:wght@400;700&display=swap">
<style>
  :root {
    --brand-blue: #1467b3;
    --brand-blue-deep: #0d5596;
    --band-grey: #5b5e63;
    --white: #ffffff;
    --logo-grey: #5f6368;
    --skin-light: #b58a73;
    --skin-dark: #4a3a33;
  }
  * { margin: 0; padding: 0; box-sizing: border-box; }
  html, body { width: 1200px; height: 2908px; overflow: hidden; background: var(--white); }
  body { font-family: "Arimo", Arial, sans-serif; }
  .banner { position: relative; width: 1200px; height: 2908px; overflow: hidden; background: var(--white); }

  .hero-photo {
    position: absolute; left: 0; top: 0; width: 1200px; height: 1560px;
    background: linear-gradient(160deg, var(--skin-dark) 0%, #6d5346 30%, var(--skin-light) 55%, #8a6553 80%, #5a463c 100%);
  }
  .panel-shape { position: absolute; left: 0; top: 0; width: 1200px; height: 2641px; }

  .services-tab {
    position: absolute; left: 0; top: 946px; height: 82px; width: 815px;
    background: var(--white);
    clip-path: polygon(0 0, 770px 0, 815px 100%, 0 100%);
    color: var(--brand-blue); font-weight: 700; font-size: 43px;
    display: flex; align-items: center; padding-left: 22px; letter-spacing: 0.3px;
  }

  .service-list { position: absolute; left: 0; top: 1145px; width: 1164px; list-style: none; text-align: center; }
  .service-list li {
    color: var(--white); font-weight: 700; font-size: 48px; line-height: 131px; letter-spacing: 0.5px;
  }

  .photo-strip { position: absolute; left: 0; top: 1838px; width: 1200px; height: 285px; display: flex; gap: 8px; }
  .photo-strip .photo { flex: 1; }
  .photo--acupuncture { background: linear-gradient(135deg, #e9e4e0, #c9a28c 50%, #b9322f 75%, #e4ddd8); }
  .photo--neck { background: linear-gradient(135deg, #d8d3cf, #a98571 45%, #3d3432 80%, #2b2726); }
  .photo--cupping { background: linear-gradient(135deg, #e9c9a7, #c8946f 50%, #f0e2d1 100%); }
  .strip-frame { position: absolute; left: 0; top: 1800px; width: 1200px; height: 360px; }

  .contact { position: absolute; left: 0; width: 1200px; text-align: center; color: var(--white); font-weight: 700; }
  .contact--lead { top: 2240px; font-size: 39px; }
  .contact--phone, .contact--web { display: flex; align-items: center; justify-content: center; gap: 26px; }
  .contact--phone { top: 2372px; font-size: 56px; }
  .contact--web { top: 2494px; font-size: 52px; }
  .contact svg { flex: none; }

  .brand-footer {
    position: absolute; left: 0; top: 2641px; width: 1200px; height: 267px;
    display: flex; align-items: center; justify-content: center; gap: 28px;
  }
  .brand-footer .brand-dot { width: 70px; height: 70px; border-radius: 50%; background: var(--brand-blue); }
  .brand-footer .brand-name { font-size: 82px; font-weight: 400; color: var(--brand-blue); letter-spacing: 1px; }
</style>
</head>
<body>
<main class="banner">
  <div class="hero-photo" role="img" aria-label="Photograph of a practitioner using a steel soft-tissue tool across a patient's upper back and shoulder"></div>

  <svg class="panel-shape" viewBox="0 0 1200 2641" aria-hidden="true">
    <path d="M0,628 C520,590 1050,930 1200,1290 L1200,2641 L0,2641 Z" fill="var(--band-grey)"/>
    <path d="M0,628 C520,590 1050,930 1200,1290" fill="none" stroke="var(--white)" stroke-width="4"/>
    <path d="M0,727 C520,700 1020,1000 1200,1515 L1200,2641 L0,2641 Z" fill="var(--brand-blue)"/>
    <path d="M0,727 C520,700 1020,1000 1200,1515" fill="none" stroke="var(--white)" stroke-width="3"/>
  </svg>

  <div class="services-tab">GENERAL SERVICES OFFERED</div>

  <ul class="service-list">
    <li>SHOCKWAVE</li>
    <li>CHIROPRACTIC</li>
    <li>ACUPUNCTURE</li>
    <li>LASER THERAPHY</li>
    <li>MASSAGE THERAPHY</li>
  </ul>

  <div class="photo-strip">
    <div class="photo photo--acupuncture" role="img" aria-label="Photo of acupuncture needles being placed in a patient's wrist"></div>
    <div class="photo photo--neck" role="img" aria-label="Photo of a chiropractor adjusting a patient's neck"></div>
    <div class="photo photo--cupping" role="img" aria-label="Photo of cupping therapy on a patient's back"></div>
  </div>
  <svg class="strip-frame" viewBox="0 0 1200 360" aria-hidden="true">
    <path d="M0,38 C400,16 800,16 1200,38 L1200,0 L0,0 Z" fill="var(--brand-blue)"/>
    <path d="M0,38 C400,16 800,16 1200,38" fill="none" stroke="var(--white)" stroke-width="5"/>
    <path d="M0,323 C400,345 800,345 1200,323 L1200,360 L0,360 Z" fill="var(--brand-blue)"/>
    <path d="M0,323 C400,340 800,340 1200,323 L1200,332 C800,352 400,352 0,332 Z" fill="var(--band-grey)"/>
    <path d="M0,323 C400,340 800,340 1200,323" fill="none" stroke="var(--white)" stroke-width="4"/>
  </svg>

  <p class="contact contact--lead">For More Information Please Contact Us:</p>
  <p class="contact contact--phone">
    <svg width="50" height="40" viewBox="0 0 50 40" aria-hidden="true">
      <path d="M3,14 C3,4 47,4 47,14 L47,18 L36,18 L36,12 L14,12 L14,18 L3,18 Z" fill="var(--white)"/>
      <path d="M12,20 L38,20 L44,38 L6,38 Z" fill="var(--white)"/>
      <circle cx="25" cy="29" r="5" fill="var(--brand-blue)"/>
    </svg>
    <span>(403) 555-0142</span>
  </p>
  <p class="contact contact--web">
    <svg width="46" height="46" viewBox="0 0 46 46" aria-hidden="true" fill="none" stroke="var(--white)" stroke-width="4">
      <circle cx="23" cy="23" r="20"/>
      <ellipse cx="23" cy="23" rx="9" ry="20"/>
      <line x1="3" y1="23" x2="43" y2="23"/>
      <line x1="23" y1="3" x2="23" y2="43"/>
    </svg>
    <span>http://www.brightwayhealth.ca/</span>
  </p>

  <footer class="brand-footer">
    <span class="brand-dot" aria-hidden="true"></span>
    <span class="brand-name">Brightway Health</span>
  </footer>
</main>
</body>
</html>
```